Design cd cover for the vocal group: Ember, cd title Harbor Light. Cd cover is for EP release to be followed by full album. Songs are: Sizwe Langa Khona(Lift high the lamp); Cold River Road; Ngolwazi(Guide me through the night); When Rain Falls. There is no track entitled harbor light; the concept of the sound of gospel music as embodied in the music tracks - contemporary and traditional - is the basis of the album title.
NB: Project can close Tuesday 12 November to account for the 5 days as I do not count Saturday as a working day.
Hey guys,
Hello to everyone. I would like to take this opportunity to say thank you for your participation. Your submissions have been great and much appreciated. Forgive me for not being able to provide feedback to all of you. The time has come for me to make selection decisions and I would like to say thank you to all for your participation, you have been great and amazing.

```html
<!DOCTYPE html>
<html lang="en">
<head>
<meta charset="utf-8">
<title>Ember – Harbor Light EP Cover</title>
<link rel="stylesheet" href="https://fonts.googleapis.com/css2?family=Yellowtail&family=Mr+Dafoe&family=Marcellus&display=swap">
<style>
  :root {
    --backdrop: #5a5a5a;
    --sky-top: #8e6f9c;
    --sky-rose: #d9727a;
    --sky-flame: #ef8a52;
    --horizon-gold: #f6c24a;
    --sea-rose: #c98a9c;
    --sea-mauve: #a97e98;
    --sea-deep: #b28aa3;
    --title-white: #ffffff;
    --subtitle-crimson: #c4213f;
    --track-white: #f7f1f4;
  }
  * { margin: 0; padding: 0; box-sizing: border-box; }
  html, body {
    width: 1200px;
    height: 1000px;
    overflow: hidden;
    background: var(--backdrop);
  }
  .canvas {
    position: relative;
    width: 1200px;
    height: 1000px;
    display: flex;
    align-items: center;
    justify-content: center;
  }
  .cover {
    position: relative;
    width: 860px;
    height: 860px;
    overflow: hidden;
  }
  .cover-scene {
    position: absolute;
    inset: 0;
    background:
      linear-gradient(180deg,
        var(--sky-top) 0%,
        #b27490 14%,
        var(--sky-rose) 30%,
        var(--sky-flame) 42%,
        var(--horizon-gold) 49%,
        #e69a78 50.5%,
        var(--sea-rose) 54%,
        var(--sea-mauve) 68%,
        var(--sea-deep) 100%);
  }
  .band-name {
    position: absolute;
    left: 46px;
    top: 40px;
    font-family: "Yellowtail", cursive;
    font-size: 210px;
    line-height: 1;
    color: var(--title-white);
    letter-spacing: -2px;
  }
  .album-title {
    position: absolute;
    left: 100px;
    top: 268px;
    font-family: "Mr Dafoe", cursive;
    font-size: 66px;
    line-height: 1;
    color: var(--subtitle-crimson);
  }
  .album-title .second-word {
    position: relative;
    top: 32px;
    margin-left: -6px;
  }
  .lead-track {
    position: absolute;
    left: 47px;
    bottom: 44px;
    font-family: "Marcellus", serif;
    font-size: 20px;
    color: var(--track-white);
    letter-spacing: 0.3px;
  }
</style>
</head>
<body>
<main class="canvas">
  <section class="cover">
    <div class="cover-scene" role="img" aria-label="Long-exposure photograph of a sunset over a calm sea, pink and purple clouds above a golden horizon, with a dark rock outcrop on the left"></div>
    <h1 class="band-name">Ember</h1>
    <h2 class="album-title">Harbor<span class="second-word">Light</span></h2>
    <p class="lead-track">Sizwe Langa Khona</p>
  </section>
</main>
</body>
</html>
```